Sophisticated, clean website reflecting my feminine, playful side to sell my abstract art,

I need a website no more than 3 pages to showcase my paintings, a little about me and some contact info. I do abstracts so looking for something a little edgy, yet feminine and current.
Updates

Hi there, These are some artists websites that I Iike: Marlowevint.com (I like how airy it is) rupertalcombe.com gideonparvell.com (I like how it scrolls) I'll need a place for a photo ( a headshot-i do not have it yet so I'll need to be able to upload that later) as well as an area for my bio. Also, it's important that I will be able to upload any new photos and descriptions easily so it should be user friendly. Lastly, I like in a sunny place so would like to have this seem upbeat and playful as that is how i like to paint. thanks-I'm trying to upload my photos now -

Target Market(s)

ppl ages 35-70 who want large scale art for their homes

Industry/Entity Type

art

Coding

Coded - Design and coding required

Number of Pages Required

3 page

Colors

Designer to choose colors to be used in the design.

Requirements
Must have
• photos of my art, a place for my bio, be easy to reach me. tasteful-nothing too "in your face" -my clients are pretty high end and organized. They like clean lines
Nice to have
• sophisticated background, muted tones in the back-similar clean font throughout-no cursive
Should not have
• too many dark areas. Too many blocks of color. Too serious.

```html
<!DOCTYPE html>
<html lang="en">
<head>
<meta charset="utf-8">
<title>Delia Marchetti — About</title>
<link href="https://fonts.googleapis.com/css2?family=Oswald:wght@200;300;400&family=Baloo+2:wght@400;500&display=swap" rel="stylesheet">
<style>
  :root {
    --paper: #f0ece5;
    --ink: #141414;
    --text: #2b2b2b;
    --muted: #444444;
    --rule: #6f6f6f;
    --photo-light: #dfe3e6;
    --photo-mid: #c9b8a8;
    --photo-warm: #8a6a55;
  }
  * { box-sizing: border-box; margin: 0; padding: 0; }
  html, body { width: 1200px; height: 858px; overflow: hidden; }
  body {
    position: relative;
    background: var(--paper);
    color: var(--text);
    font-family: "Baloo 2", sans-serif;
  }
  .site-header {
    position: absolute; top: 0; left: 0; width: 1200px; height: 170px;
  }
  .brand {
    position: absolute; top: 40px; left: 0; width: 1200px;
    display: flex; justify-content: center; align-items: center; gap: 10px;
    font-family: "Oswald", sans-serif; font-weight: 300;
    font-size: 16px; letter-spacing: 1px; color: var(--ink);
  }
  .brand-square { width: 14px; height: 14px; background: var(--ink); }
  .brand-rule {
    position: absolute; top: 109px; left: 514px; width: 172px;
    border-top: 1px solid var(--rule);
  }
  .main-nav {
    position: absolute; top: 132px; left: 0; width: 1200px; height: 30px;
  }
  .main-nav a {
    position: absolute; top: 0; transform: translateX(-50%);
    font-family: "Oswald", sans-serif; font-weight: 200; font-size: 20px;
    color: var(--ink); text-decoration: none; letter-spacing: 0.3px;
  }
  .main-nav a.is-current { font-weight: 400; }
  .nav-gallery { left: 457px; }
  .nav-about { left: 599px; }
  .nav-contact { left: 742px; }

  .portrait {
    position: absolute; top: 242px; left: 42px; width: 405px; height: 516px;
    border: 2px solid var(--ink);
    background: linear-gradient(160deg, var(--photo-light) 0%, var(--photo-light) 35%, var(--photo-mid) 65%, var(--photo-warm) 100%);
  }
  .bio {
    position: absolute; top: 342px; left: 485px; width: 460px;
    font-size: 13.2px; line-height: 20.8px; color: var(--text);
  }
  .tagline {
    position: absolute; top: 521px; left: 485px;
    display: flex; align-items: center; gap: 9px;
    font-size: 13px; font-weight: 500; color: var(--ink);
  }
  .tagline::before {
    content: ""; width: 8px; height: 8px; border-radius: 50%; background: var(--ink);
  }
  .email {
    position: absolute; top: 581px; left: 485px;
    display: flex; align-items: center; gap: 10px;
    font-size: 13.2px; color: var(--text);
  }
  .social {
    position: absolute; top: 622px; left: 485px; display: flex; gap: 25px;
  }
  .social-link {
    width: 29px; height: 29px; border: 1.5px solid var(--ink); border-radius: 50%;
  }
  .site-footer {
    position: absolute; top: 826px; left: 0; width: 1200px; text-align: center;
    font-size: 11px; color: var(--muted);
  }
</style>
</head>
<body>
  <header class="site-header">
    <div class="brand"><span class="brand-square"></span><span>DELIA MARCHETTI</span></div>
    <div class="brand-rule"></div>
    <nav class="main-nav">
      <a class="nav-gallery" href="#">GALLERY</a>
      <a class="nav-about is-current" href="#">ABOUT</a>
      <a class="nav-contact" href="#">CONTACT</a>
    </nav>
  </header>

  <main>
    <div class="portrait" role="img" aria-label="Headshot of the artist smiling in a white t-shirt against a pale wall"></div>

    <p class="bio">
      Delia Marchetti is a southern California based artist working with acrylic<br>
      on canvas. Self taught with a favoritism toward large scale pieces,<br>
      Delia has been creating works since she could hold a brush.<br>
      Often caught drawing on legs during class, walls while talking on the phone<br>
      and always carrying a pen to draw out her thoughts, she has truly grown up<br>
      expressing who she is through the tools of the artist. She enjoys losing<br>
      herself within the canvas and embraces raw emotion in hopes of spilling<br>
      out into the piece.
    </p>

    <p class="tagline">Bold-vibrant-daring-emotional-still</p>

    <p class="email">
      <svg width="18" height="14" viewBox="0 0 18 14" aria-hidden="true">
        <rect x="0" y="0" width="18" height="14" rx="1.5" fill="#141414"/>
        <path d="M1.5 2 L9 7.5 L16.5 2" fill="none" stroke="#f0ece5" stroke-width="1.6"/>
      </svg>
      contact@DeliaMarchettiAbstract.com
    </p>

    <div class="social">
      <a class="social-link" href="#" aria-label="Social profile one"></a>
      <a class="social-link" href="#" aria-label="Social profile two"></a>
    </div>
  </main>

  <footer class="site-footer">©2022 Delia Marchetti Art. All rights reserved.</footer>
</body>
</html>
```